TOASTED COCONUT CHIPS

My company is a food company specialised in coconut products. The subject project is to design the package bag and respective simple shipping case for toasted coconut chips for two flavors: one is original and the other is cinnamon. I also need a logo design for the brand "pelvo".

I would like the bag looks simple, classy and attractive. Or the other way that it could look cute and fun.

The design will include two flavors: original/sea salt and cinnamon
The design need to be fit in 40g pouch bag and 20g bag.
Need the design of the bag and subsequently the shipping case.
Updates

Project Deadline Extended Reason: As per request of some designers, the deadline will be extended by 5 days. Added Tuesday, November 8, 2016

Target Market(s)

age 8 to 40
sell in cafeteria and vending machine

Industry/Entity Type

It Company

Logo Text

simple and direct

Requirements
Must have
• golden coconut chips picture on the front side.
• the bag should looks clean but attractive.
• Otherwise, it has to be very colourful to attract eye balls.
• I need the design can be fit in a 40g pouch and 20g cutie size bag
Should not have
• Should not look Asian food.

```html
<!DOCTYPE html>
<html lang="en">
<head>
<meta charset="utf-8">
<title>Pelvo Toasted Coconut Chips – Original Flavour</title>
<link rel="stylesheet" href="https://fonts.googleapis.com/css2?family=Archivo+Black&family=Cinzel:wght@500;700&family=Josefin+Sans:wght@400;600&family=Lato:wght@300;400&display=swap">
<style>
  :root {
    --bag-white: #fbfbfb;
    --seal-grey: #d4d4d6;
    --seal-line: #b9b9bc;
    --brand-brown: #a3652f;
    --teal: #2bb3b1;
    --sun-yellow: #f2bd1c;
    --sun-yellow-light: #f8d04a;
    --husk-brown: #84573a;
    --toast-tan: #c69a68;
    --coconut-cream: #efe4cc;
    --chip-gold: #e6c27a;
    --ink: #2e2e2e;
    --white: #ffffff;
  }
  * { box-sizing: border-box; margin: 0; padding: 0; }
  html, body { width: 1072px; height: 1200px; overflow: hidden; background: #ececec; }
  .pouch {
    position: relative;
    width: 1072px;
    height: 1200px;
    background: var(--bag-white);
    overflow: hidden;
  }
  .pouch__seal {
    position: absolute; top: 0; left: 0; width: 100%; height: 42px;
    background: repeating-linear-gradient(to bottom, var(--seal-grey) 0 5px, var(--seal-line) 5px 7px);
  }
  .flavour-name {
    position: absolute; top: 68px; left: 74px;
    font-family: "Josefin Sans", sans-serif; font-weight: 400;
    font-size: 42px; letter-spacing: 1px; color: var(--teal);
  }
  .brand-name {
    position: absolute; top: 108px; left: 0; width: 100%;
    text-align: center;
    font-family: "Cinzel", serif; font-weight: 700;
    font-size: 150px; line-height: 1; letter-spacing: 6px;
    color: var(--brand-brown);
  }
  .product-title {
    position: absolute; top: 262px; left: 0; width: 100%;
    text-align: center;
    font-family: "Cinzel", serif; font-weight: 700;
    color: var(--teal); line-height: 1;
  }
  .product-title span { display: block; }
  .product-title__toasted { font-size: 44px; letter-spacing: 3px; margin-left: 60px; }
  .product-title__coconut { font-size: 84px; letter-spacing: 6px; margin-top: 6px; margin-left: 60px; }
  .product-title__chips { font-size: 64px; letter-spacing: 6px; margin-top: 6px; margin-left: 60px; }
  .lower-panel {
    position: absolute; top: 760px; left: 0; width: 100%; height: 440px;
    background: linear-gradient(160deg, var(--sun-yellow-light), var(--sun-yellow));
  }
  .hero-photo {
    position: absolute; top: 478px; left: 40px; width: 992px; height: 310px;
    border-radius: 24px;
    background: linear-gradient(90deg, var(--husk-brown) 0%, var(--toast-tan) 30%, var(--coconut-cream) 55%, var(--chip-gold) 100%);
  }
  .description-band {
    position: absolute; top: 800px; left: 0; width: 100%; height: 112px;
    background: var(--teal);
    padding: 16px 60px 0 110px;
    font-family: "Lato", sans-serif; font-weight: 400;
    font-size: 21px; line-height: 1.3; color: var(--white);
  }
  .claims {
    position: absolute; top: 950px; list-style: none;
    font-family: "Archivo Black", sans-serif; font-size: 27px;
    color: var(--ink); line-height: 1;
  }
  .claims--left { left: 80px; }
  .claims--right { left: 580px; font-size: 25px; }
  .claims li { display: flex; align-items: center; height: 40px; }
  .claims svg { width: 22px; height: 22px; margin-right: 14px; flex: none; }
  .net-weight {
    position: absolute; top: 1160px; right: 60px;
    font-family: "Lato", sans-serif; font-size: 16px; color: var(--ink);
  }
</style>
</head>
<body>
<main class="pouch">
  <div class="pouch__seal"></div>

  <p class="flavour-name">Original Flavour</p>
  <h1 class="brand-name">PELVO</h1>
  <h2 class="product-title">
    <span class="product-title__toasted">TOASTED</span>
    <span class="product-title__coconut">COCONUT</span>
    <span class="product-title__chips">CHIPS</span>
  </h2>

  <div class="lower-panel"></div>
  <div class="hero-photo" role="img" aria-label="Photo of an opened coconut with green leaves beside a white bowl of golden toasted coconut chips"></div>

  <p class="description-band">Pelvo Toasted Coconut Chips are made from premium coconuts and slowly toasted to perfection. It is absolutely a tasty and healthy snack on their own or as an accompaniment with salads, ice cream or yogurt.</p>

  <ul class="claims claims--left">
    <li><svg viewBox="0 0 24 24"><path d="M3 13l6 6L21 5" fill="none" stroke="#2e2e2e" stroke-width="3.5"/></svg>ALL NATURAL INGREDIENTS</li>
    <li><svg viewBox="0 0 24 24"><path d="M3 13l6 6L21 5" fill="none" stroke="#2e2e2e" stroke-width="3.5"/></svg>NOT FIRED</li>
    <li><svg viewBox="0 0 24 24"><path d="M3 13l6 6L21 5" fill="none" stroke="#2e2e2e" stroke-width="3.5"/></svg>100% VEGAN</li>
    <li><svg viewBox="0 0 24 24"><path d="M3 13l6 6L21 5" fill="none" stroke="#2e2e2e" stroke-width="3.5"/></svg>GLUTEN FREE</li>
    <li><svg viewBox="0 0 24 24"><path d="M3 13l6 6L21 5" fill="none" stroke="#2e2e2e" stroke-width="3.5"/></svg>DAIRY FREE</li>
  </ul>

  <ul class="claims claims--right">
    <li><svg viewBox="0 0 24 24"><path d="M3 13l6 6L21 5" fill="none" stroke="#2e2e2e" stroke-width="3.5"/></svg>NO CHOLESTEROL</li>
    <li><svg viewBox="0 0 24 24"><path d="M3 13l6 6L21 5" fill="none" stroke="#2e2e2e" stroke-width="3.5"/></svg>NO PRESERVATIVE</li>
    <li><svg viewBox="0 0 24 24"><path d="M3 13l6 6L21 5" fill="none" stroke="#2e2e2e" stroke-width="3.5"/></svg>NO ARTIFICAL COLOR</li>
    <li><svg viewBox="0 0 24 24"><path d="M3 13l6 6L21 5" fill="none" stroke="#2e2e2e" stroke-width="3.5"/></svg>NO ARTIFICIAL FLAVOURING</li>
    <li><svg viewBox="0 0 24 24"><path d="M3 13l6 6L21 5" fill="none" stroke="#2e2e2e" stroke-width="3.5"/></svg>GOOD SOURCE OF FIBER</li>
  </ul>

  <p class="net-weight">Net weight: 20 g (0.7 oz)</p>
</main>
</body>
</html>
```